New design for Gift Ledger Website - landing page plus 3 carousel pages

We have a new website we want to launch for 501c3 organizations - Faith-based organizations, not for profit organizations, colleges and universities. Note - this is a design only project. We want to see designs for the landing page and the 3 other pages - Faith-based organizations, not for profit organizations, colleges and universities.
Format: We expect to create this website in Wix so requirement is to make the graphics Wix compatible
See Dossier attached for more details, 4 wireframes (1 landing page and 3 carousel pages), and brand guidelines
Please be creative and and make the visuals engaging. We do NOT want you to simply replicate what is in the wireframe. We are looking for a totally new, fresh and engaging design.
Look and feel
Each slider illustrates characteristics of the customer's brand and the style your logo design should communicate.

```html
<!DOCTYPE html>
<html lang="en">
<head>
<meta charset="utf-8">
<title>Givora – 501C3 Organization</title>
<link rel="stylesheet" href="https://fonts.googleapis.com/css2?family=Comfortaa:wght@300;400;700&family=Montserrat:wght@300;400;500;600;700&display=swap">
<style>
:root{
  --bg:#0b1024;
  --bg-deep:#0a0e1f;
  --hero-blue:#0f2452;
  --teal:#00c4a0;
  --line:#2e3a4a;
  --text:#ffffff;
  --muted:#c9d3dc;
}
*{box-sizing:border-box;margin:0;padding:0}
html,body{width:1200px;height:4167px;overflow:hidden}
body{
  position:relative;
  background:linear-gradient(180deg,var(--hero-blue) 0%,#0c1838 14%,var(--bg) 26%,var(--bg) 100%);
  color:var(--text);
  font-family:"Montserrat",sans-serif;
}
.abs{position:absolute}
.round{font-family:"Comfortaa",sans-serif}

/* header */
.site-header{left:0;top:0;width:1200px;height:110px;border-bottom:1px solid rgba(0,196,160,.5)}
.brand{left:95px;top:34px;font-size:30px;font-weight:700;line-height:40px}
.main-nav{left:506px;top:48px;font-size:11px;letter-spacing:.4px}
.main-nav a{position:absolute;color:#fff;text-decoration:none;white-space:nowrap}
.main-nav a.active::after{content:"";position:absolute;left:0;right:0;bottom:-8px;height:2px;background:var(--teal)}
.login{left:1014px;top:0;width:186px;height:110px;background:var(--teal);display:flex;align-items:center;justify-content:center;font-size:14px;font-weight:500;color:#0b1e3a}

/* hero */
.hero-title{left:95px;top:226px;font-family:"Comfortaa",sans-serif;font-weight:300;font-size:66px;line-height:66px;color:var(--teal)}
.hero-title .fade{background:linear-gradient(90deg,var(--teal) 40%,#1b54c9);-webkit-background-clip:text;background-clip:text;color:transparent}
.hero-copy{left:95px;top:375px;width:600px;font-size:15px;line-height:20px;font-weight:400}
.hero-art{left:711px;top:218px;width:390px;height:380px;border-radius:50%;
  background:radial-gradient(ellipse at 55% 45%,rgba(0,196,160,.35),rgba(16,70,130,.25) 55%,transparent 72%)}

/* audiences */
.icon-box{width:127px;height:114px;border:1px solid var(--line);display:flex;align-items:center;justify-content:center;
  font-family:"Comfortaa",sans-serif;font-weight:700;font-size:32px;color:var(--teal)}
.audience-label{font-size:15px;font-weight:700;line-height:20px;color:var(--teal)}
.audience-label .more{display:inline-block;margin-top:4px;font-weight:400;color:#fff;font-size:17px;border-bottom:2px solid var(--teal);padding-bottom:2px}

.tri-label{font-weight:700;font-size:18px;line-height:20px;text-align:center;color:var(--teal)}

/* process */
.section-title{left:0;width:1200px;text-align:center;font-family:"Comfortaa",sans-serif;font-weight:700;color:var(--teal)}
.step{width:300px;padding:22px 22px;border:1px solid var(--line)}
.step.filled{background:linear-gradient(180deg,#04a98c 0%,#0a6d66 45%,#0b2f3a 100%);border-color:#1d4d52}
.step.outline{background:var(--bg-deep);border-color:#54606e}
.step h3{font-family:"Comfortaa",sans-serif;font-weight:700;font-size:25px;margin-bottom:24px}
.step.outline h3{color:var(--teal)}
.step p{font-size:13px;line-height:18.4px;text-align:justify;font-weight:500}

.btn{background:var(--teal);color:#0b1e3a;font-size:17px;font-weight:400;display:flex;align-items:center;justify-content:center}

/* donation */
.amount{width:154px;height:58px;border:1px solid var(--teal);display:flex;align-items:center;justify-content:center;
  font-family:"Comfortaa",sans-serif;font-weight:700;font-size:25px;color:var(--teal)}
.amount.selected{background:var(--teal);color:#0b1e3a}
.amount.other{font-weight:300;font-size:24px;line-height:29px;text-align:center}
.partner{width:154px;height:137px;border:1px solid var(--line);display:flex;align-items:center;justify-content:center;
  font-family:"Comfortaa",sans-serif;font-weight:700;font-size:33px;color:var(--teal)}

/* ways to donate */
.panel-image{display:flex;align-items:center;justify-content:center;font-family:"Comfortaa",sans-serif;font-weight:700;font-size:32px}
.panel-text{text-align:center;font-size:15px;line-height:21px}
.mini-btn{background:var(--teal);color:#0b1e3a;font-size:16px;height:28px;width:146px;display:flex;align-items:center;justify-content:center}

.video{left:102px;top:2825px;width:996px;height:558px;border:2px solid var(--teal);box-shadow:0 0 12px rgba(0,196,160,.25)}

.feature-label{font-size:15px;font-weight:700;color:var(--teal)}
.feature-label small{display:block;font-size:11px;font-weight:400;line-height:16px;margin-top:3px}

.signup{left:344px;top:3768px;width:510px;height:52px;display:flex;box-shadow:0 0 14px rgba(0,196,160,.35)}
.signup .field{flex:1;border:1px solid var(--teal);display:flex;align-items:center;padding-left:24px;font-size:14px;color:var(--muted)}
.signup .send{width:110px;background:var(--teal);color:#0b1e3a;display:flex;align-items:center;justify-content:center;letter-spacing:7px;font-size:14px}
.teal-copy{left:0;width:1200px;text-align:center;color:var(--teal)}
</style>
</head>
<body>

<header class="site-header abs">
  <div class="brand abs">Givora</div>
  <nav class="main-nav abs">
    <a class="active" style="left:0">ABOUT US</a>
    <a style="left:100px">NEWSROOM</a>
    <a style="left:197px">PARENTS</a>
    <a style="left:280px">CLIENTS</a>
    <a style="left:357px">FAQ</a>
    <a style="left:408px">CONTACT</a>
  </nav>
  <div class="login abs">LOGIN</div>
</header>

<h1 class="hero-title abs">501C3<br><span class="fade">ORGANIZATION</span></h1>
<p class="hero-copy abs">Lorem Ipsum is simply dummy text of the printing and typesetting industry. Lorem Ipsum has been the industry's standard dummy text ever since the 1500s, when an unknown printer took a galley of type and scrambled it to make a type specimen book. It has survived not only five centuries, but also the leap into electronic typesetting.</p>
<div class="hero-art abs" role="img" aria-label="Abstract teal particle ring illustration"></div>

<div class="icon-box abs" style="left:102px;top:679px">icon</div>
<div class="audience-label abs" style="left:243px;top:704px">Non Profit<br>Organiozation<br><span class="more">More</span></div>
<div class="icon-box abs" style="left:446px;top:679px">icon</div>
<div class="audience-label abs" style="left:587px;top:704px">Faith<br>Base<br><span class="more">More</span></div>
<div class="icon-box abs" style="left:792px;top:679px">icon</div>
<div class="audience-label abs" style="left:933px;top:704px">Colleges and<br>Universities<br><span class="more">More</span></div>

<div class="tri-label abs" style="left:500px;top:897px;width:200px">501C3<br>ORGANIZATION</div>
<div class="tri-label abs" style="left:333px;top:1083px;width:150px">DATA OBJECT<br>“DONOR”</div>
<div class="tri-label abs" style="left:704px;top:1083px;width:180px">DATA EXCHANGE<br>“BUYER”</div>
<svg class="abs" style="left:340px;top:940px" width="520" height="330" viewBox="0 0 520 330" aria-hidden="true">
  <defs>
    <radialGradient id="floorGlow" cx="50%" cy="50%" r="50%">
      <stop offset="0" stop-color="#1d4fff" stop-opacity=".9"/>
      <stop offset="1" stop-color="#1d4fff" stop-opacity="0"/>
    </radialGradient>
    <filter id="lineGlow"><feGaussianBlur stdDeviation="4"/></filter>
  </defs>
  <ellipse cx="260" cy="307" rx="240" ry="14" fill="url(#floorGlow)"/>
  <polygon points="100,22 418,22 260,297" fill="none" stroke="#7ad7ff" stroke-width="6" opacity=".45" filter="url(#lineGlow)"/>
  <polygon points="100,22 418,22 260,297" fill="none" stroke="#fff" stroke-width="2.5"/>
</svg>

<h2 class="section-title abs" style="top:1333px;font-size:32px">PROCESS</h2>

<article class="step filled abs" style="left:0;top:1407px;height:299px"><h3>01 Step</h3><p>Lorem Ipsum is simply dummy text of the printing and typesetting industry. Lorem Ipsum has been the industry's standard dummy text ever since the 1500s, when an unknown printer took a galley of type and scrambled it to make a type specimen book. It has survived not only five centuries, but also the leap into electronic typesetting.</p></article>
<article class="step outline abs" style="left:300px;top:1391px;height:299px"><h3>02 Step</h3><p>Lorem Ipsum is simply dummy text of the printing and typesetting industry. Lorem Ipsum has been the industry's standard dummy text ever since the 1500s, when an unknown printer took a galley of type and scrambled it to make a type specimen book. It has survived not only five centuries, but also the leap into electronic typesetting.</p></article>
<article class="step filled abs" style="left:600px;top:1407px;height:299px"><h3>03 Step</h3><p>Lorem Ipsum is simply dummy text of the printing and typesetting industry. Lorem Ipsum has been the industry's standard dummy text ever since the 1500s, when an unknown printer took a galley of type and scrambled it to make a type specimen book. It has survived not only five centuries, but also the leap into electronic typesetting.</p></article>
<article class="step outline abs" style="left:900px;top:1391px;height:299px"><h3>04 Step</h3><p>Lorem Ipsum is simply dummy text of the printing and typesetting industry. Lorem Ipsum has been the industry's standard dummy text ever since the 1500s, when an unknown printer took a galley of type and scrambled it to make a type specimen book. It has survived not only five centuries, but also the leap into electronic typesetting.</p></article>

<div class="btn abs" style="left:450px;top:1746px;width:299px;height:57px">Donate Data</div>

<h2 class="section-title abs" style="top:1884px;font-size:29px">My Donation</h2>
<p class="teal-copy abs" style="top:1928px;font-size:15px">All donations are tax deductible</p>
<p class="teal-copy abs round" style="top:1966px;font-size:23px">I want to give</p>

<div class="amount selected abs" style="left:99px;top:2028px">$25</div>
<div class="amount abs" style="left:267px;top:2028px">$50</div>
<div class="amount abs" style="left:437px;top:2028px">$100</div>
<div class="amount abs" style="left:606px;top:2028px">$125</div>
<div class="amount abs" style="left:775px;top:2028px">$150</div>
<div class="amount other abs" style="left:944px;top:2028px;border-color:#5fd6bf">Other<br>Amount</div>

<div class="partner abs" style="left:186px;top:2138px">Logo</div>
<div class="partner abs" style="left:354px;top:2138px">Logo</div>
<div class="partner abs" style="left:522px;top:2138px">Logo</div>
<div class="partner abs" style="left:690px;top:2138px">Logo</div>
<div class="partner abs" style="left:859px;top:2138px">Logo</div>

<div class="btn abs" style="left:450px;top:2338px;width:299px;height:57px">Donate with credit card</div>

<div class="panel-image abs" role="img" aria-label="Image about donating with crypto" style="left:0;top:2458px;width:300px;height:283px;background:linear-gradient(180deg,#0a6a64 0%,#079e87 60%,#0b8d7c 100%)">image</div>
<div class="abs" style="left:300px;top:2443px;width:299px;height:298px;border:1px solid #54606e;background:var(--bg-deep)">
  <p class="panel-text abs" style="left:0;top:78px;width:297px">Donate with Crypto<br>Powered by GVR</p>
  <div class="abs" style="left:0;top:140px;width:297px;text-align:center;font-weight:700;font-size:15px">Givora</div>
  <div class="mini-btn abs" style="left:76px;top:191px">Donate</div>
</div>
<div class="abs" style="left:600px;top:2464px;width:600px;height:301px;border:1px solid #54606e;background:var(--bg-deep)">
  <div class="panel-image abs" role="img" aria-label="Image about donating with data" style="left:0;top:0;width:299px;height:299px;background:linear-gradient(180deg,#0b6e6a 0%,#0b3a45 55%,var(--bg-deep) 100%)">image</div>
  <p class="panel-text abs" style="left:300px;top:85px;width:300px">Donate with Data</p>
  <div class="mini-btn abs" style="left:378px;top:197px">Donate</div>
</div>

<div class="video abs">
  <svg class="abs" style="left:458px;top:245px" width="86" height="96" viewBox="0 0 86 96" aria-label="Play video" role="img"><polygon points="0,0 86,48 0,96" fill="#00c4a0"/></svg>
</div>

<h2 class="section-title abs" style="top:3453px;font-size:29px">Why Enroll!</h2>
<p class="teal-copy abs" style="top:3497px;font-size:14.5px">To get full access to all the features start by creating an account</p>

<div class="icon-box abs" style="left:102px;top:3546px">icon</div>
<div class="feature-label abs" style="left:243px;top:3570px;width:170px">Drops<small>To get full access to all the features start by creating an account</small></div>
<div class="icon-box abs" style="left:446px;top:3546px">icon</div>
<div class="feature-label abs" style="left:587px;top:3570px;width:170px">Marketplace<small>To get full access to all the features start by creating an account</small></div>
<div class="icon-box abs" style="left:792px;top:3546px">icon</div>
<div class="feature-label abs" style="left:933px;top:3570px;width:170px">My NFTs<small>To get full access to all the features start by creating an account</small></div>

<h2 class="section-title abs" style="top:3712px;font-size:29px">Get notified about new amazing products</h2>
<form class="signup abs"><div class="field">Email</div><div class="send">SEND</div></form>

<h2 class="section-title abs" style="top:3880px;font-size:29px">Never miss a drop</h2>
<p class="teal-copy abs round" style="top:3914px;font-size:27px;line-height:37px;left:300px;width:600px">Subscribe for the latest news, drops &amp; collectibles</p>
<p class="teal-copy abs" style="top:4022px;left:280px;width:640px;font-size:15px;line-height:20px">After reading the Privacy Notice, you may subscribe for our newsletter to get special offers and occasional surveys delivered to your inbox. Unsubscribe at any time by clicking on the link in the mail.</p>
<p class="abs" style="left:312px;top:4107px;font-size:15px;color:var(--teal);display:flex;align-items:center;gap:10px"><span style="width:14px;height:14px;background:var(--teal)"></span>By entering my email and subscribing i confirm and agree to the above.</p>

</body>
</html>
```